Accounting business needs a fridge magnet design

I need a business card size design to be used as a fridge magnet.
It will need to be vertical not horizontal and it will have my logo and the services I provide listed below it.
It needs to be pleasing to the eye and catch peoples attention.
I have uploaded my current business card as a reference.
It can look totally different though, i am open to new ideas.

It will need to say:

Specialising in:
*Small Business Taxation
*Company & Trust Returns
*Financial Statements
*Partnership Taxation
*BAS preparation/lodgement
*Capital Gains Tax
*Business Start Ups
*Business Structuring
*Tax Planning

```html
<!DOCTYPE html>
<html lang="en">
<head>
<meta charset="utf-8">
<title>Nova Tax – Fridge Magnet</title>
<link href="https://fonts.googleapis.com/css2?family=Poppins:wght@400;600&family=Roboto:wght@400&display=swap" rel="stylesheet">
<style>
  :root {
    --backdrop: #a9a9a9;
    --card-dark: #2a2b2d;
    --card-light: #ffffff;
    --ink-light: #ffffff;
    --ink-silver: #d9d9d9;
    --ink-dark: #333333;
    --badge-neutral: #e2e2e2;
  }
  * { margin: 0; padding: 0; box-sizing: border-box; }
  html, body {
    width: 1200px;
    height: 1200px;
    overflow: hidden;
    background: var(--backdrop);
  }
  .magnet {
    position: absolute;
    left: 257px;
    top: 40px;
    width: 686px;
    height: 1120px;
    background: var(--card-light);
  }
  .magnet__top {
    position: absolute;
    left: 0; top: 0;
    width: 100%;
    height: 876px;
    background: var(--card-dark);
    text-align: center;
  }
  .brand-mark {
    position: absolute;
    left: 50%;
    top: 78px;
    width: 188px;
    height: 188px;
    margin-left: -94px;
  }
  .brand-name {
    position: absolute;
    left: 0; right: 0;
    top: 296px;
    font-family: "Poppins", sans-serif;
    font-weight: 400;
    font-size: 56px;
    letter-spacing: 0.4em;
    text-indent: 0.4em;
    color: var(--ink-silver);
    line-height: 1;
  }
  .services-heading {
    position: absolute;
    left: 0; right: 0;
    top: 426px;
    font-family: "Poppins", sans-serif;
    font-weight: 600;
    font-size: 30px;
    color: var(--ink-light);
    line-height: 1.2;
  }
  .services-list {
    position: absolute;
    left: 0; right: 0;
    top: 484px;
    list-style: none;
    font-family: "Poppins", sans-serif;
    font-weight: 400;
    font-size: 30px;
    line-height: 39px;
    color: var(--ink-light);
  }
  .magnet__bottom {
    position: absolute;
    left: 0; top: 876px;
    width: 100%;
    height: 244px;
    text-align: center;
  }
  .registration-badge {
    position: absolute;
    left: 50%;
    top: 18px;
    width: 134px;
    height: 134px;
    margin-left: -67px;
  }
  .agent-details {
    position: absolute;
    left: 0; right: 0;
    top: 158px;
    font-family: "Roboto", sans-serif;
    font-size: 16px;
    line-height: 21px;
    color: var(--ink-dark);
  }
</style>
</head>
<body>
  <div class="magnet">
    <section class="magnet__top">
      <svg class="brand-mark" viewBox="0 0 188 188" aria-hidden="true">
        <circle cx="94" cy="94" r="91" fill="none" stroke="var(--ink-silver)" stroke-width="4"/>
      </svg>
      <div class="brand-name">NOVA TAX</div>
      <h2 class="services-heading">SPECIALISING IN:</h2>
      <ul class="services-list">
        <li>SMALL BUSINESS TAXATION</li>
        <li>COMPANY &amp; TRUST RETURNS</li>
        <li>FINANCIAL STATEMENTS</li>
        <li>PARTNERSHIP TAXATION</li>
        <li>BAS PREPARATION/LODGEMENT</li>
        <li>CAPITAL GAINS TAX</li>
        <li>BUSINESS START UPS</li>
        <li>BUSINESS STRUCTURING</li>
        <li>TAX PLANNING</li>
      </ul>
    </section>
    <section class="magnet__bottom">
      <svg class="registration-badge" viewBox="0 0 134 134" role="img" aria-label="Tax agent registration badge">
        <circle cx="67" cy="67" r="64" fill="var(--badge-neutral)"/>
      </svg>
      <div class="agent-details">Tax agent<br>31857290</div>
    </section>
  </div>
</body>
</html>
```